Brisk Rig Vitals: Truck Smoke Check Company

I need a logo for a truck health company in California called "Brisk Rig Vitals". This company does smoke checks for heavy duty diesel trucks under the Pacific Clean Skies Council (PCSC) called HD I/M tests. I want the brand to feel reliable.

Target Market(s)

California Diesel Trucks. Individual truck drivers and trucking companies.

Industry/Entity Type

Automotive

Contact Information for Business Card

Company Name, Slogan, contact information. marcotellez@briskrigvitals-example.com

```html
<!DOCTYPE html>
<html lang="en">
<head>
<meta charset="utf-8">
<title>Brisk Rig Vitals – Business Card</title>
<link href="https://fonts.googleapis.com/css2?family=Montserrat:wght@500;700&family=Roboto:wght@400&display=swap" rel="stylesheet">
<style>
  :root {
    --bg: #2a2c2f;
    --navy: #175d82;
    --navy-dark: #14506f;
    --sky: #3bb4e5;
    --gold: #f9b42a;
    --green: #3f9d45;
    --white: #ffffff;
    --ink: #4a4a4a;
  }
  html, body {
    margin: 0;
    width: 1200px;
    height: 800px;
    overflow: hidden;
    background: var(--bg);
  }
  .canvas {
    position: relative;
    width: 1200px;
    height: 800px;
  }
  .card {
    position: absolute;
    top: 246px;
    width: 540px;
    height: 308px;
    border-radius: 26px;
    overflow: hidden;
  }
  .card--front { left: 40px; background: var(--white); }
  .card--back  { left: 620px; background: var(--navy); }

  /* front */
  .brand {
    position: absolute;
    left: 0;
    top: 78px;
    width: 250px;
    display: flex;
    flex-direction: column;
    align-items: center;
    gap: 12px;
  }
  .brand__dot {
    width: 58px;
    height: 58px;
    border-radius: 50%;
    background: var(--navy);
  }
  .brand__name {
    font-family: "Montserrat", sans-serif;
    font-weight: 700;
    font-size: 19px;
    letter-spacing: 1.5px;
    text-transform: uppercase;
    color: var(--navy);
  }
  .divider {
    position: absolute;
    left: 262px;
    top: 64px;
    width: 1.5px;
    height: 160px;
    background: var(--gold);
  }
  .contact {
    position: absolute;
    left: 286px;
    top: 66px;
    font-family: "Roboto", sans-serif;
    color: var(--ink);
  }
  .contact__name {
    margin: 0;
    font-family: "Montserrat", sans-serif;
    font-weight: 700;
    font-size: 21px;
    color: var(--navy);
    text-transform: uppercase;
  }
  .contact__title {
    margin: 0 0 12px;
    font-family: "Montserrat", sans-serif;
    font-weight: 500;
    font-size: 14px;
    color: var(--sky);
  }
  .contact__address {
    margin: 0 0 6px;
    font-size: 14px;
    line-height: 1.3;
    font-style: normal;
  }
  .contact__line {
    display: flex;
    align-items: center;
    gap: 8px;
    font-size: 13.5px;
    line-height: 1.45;
  }
  .contact__icon { width: 14px; height: 14px; flex: none; }
  .stripes {
    position: absolute;
    left: 0;
    bottom: 0;
    width: 100%;
    height: 44px;
    background: var(--navy);
  }
  .stripes__bar {
    position: absolute;
    top: 0;
    height: 6px;
  }
  .stripes__bar--green { left: 0; width: 168px; background: var(--green); }
  .stripes__bar--gold  { left: 174px; width: 178px; background: var(--gold); }
  .stripes__bar--sky   { left: 358px; width: 182px; background: var(--sky); }
  .stripes__gap {
    position: absolute;
    top: 6px;
    left: 0;
    width: 100%;
    height: 4px;
    background: var(--white);
  }

  /* back */
  .back-brand {
    position: absolute;
    inset: 0;
    display: flex;
    flex-direction: column;
    align-items: center;
    justify-content: center;
    gap: 16px;
  }
  .back-brand__dot {
    width: 78px;
    height: 78px;
    border-radius: 50%;
    background: var(--white);
  }
  .back-brand__name {
    font-family: "Montserrat", sans-serif;
    font-weight: 700;
    font-size: 28px;
    letter-spacing: 2px;
    text-transform: uppercase;
    color: var(--white);
  }
</style>
</head>
<body>
<main class="canvas">
  <section class="card card--front" aria-label="Business card front">
    <div class="brand">
      <div class="brand__dot"></div>
      <div class="brand__name">Brisk Rig Vitals</div>
    </div>
    <div class="divider"></div>
    <div class="contact">
      <h1 class="contact__name">Marco Tellez</h1>
      <p class="contact__title">Founder &amp; CEO</p>
      <address class="contact__address">812 Harbor Ridge Lane,<br>Alder Bay CA 90000</address>
      <div class="contact__line">
        <svg class="contact__icon" viewBox="0 0 16 16" aria-hidden="true"><path fill="#3bb4e5" d="M3.6 1.2l2.3 2.6-1.3 1.9c.9 2 2.6 3.7 4.7 4.7l1.9-1.3 2.6 2.3-1.4 2.4C6.8 14.2 1.8 9.2 1.2 3z"/></svg>
        <span>555.010.4821</span>
      </div>
      <div class="contact__line">
        <svg class="contact__icon" viewBox="0 0 16 16" aria-hidden="true"><rect x="1" y="3" width="14" height="10" rx="1.5" fill="#3bb4e5"/><path d="M1.5 4l6.5 5 6.5-5" fill="none" stroke="#fff" stroke-width="1.3"/></svg>
        <span>marcotellez@briskrigvitals-example.com</span>
      </div>
    </div>
    <div class="stripes">
      <div class="stripes__gap"></div>
      <div class="stripes__bar stripes__bar--green"></div>
      <div class="stripes__bar stripes__bar--gold"></div>
      <div class="stripes__bar stripes__bar--sky"></div>
    </div>
  </section>

  <section class="card card--back" aria-label="Business card back">
    <div class="back-brand">
      <div class="back-brand__dot"></div>
      <div class="back-brand__name">Brisk Rig Vitals</div>
    </div>
  </section>
</main>
</body>
</html>
```